Banner Ad Design Project -Oil and Gas Value Chain

I am needing to create a simple graphic like the one here:

size: 720x300
http://plumwickstudio.example/designresources/banners/examples/720x300.php

Oil and Gas Value Chain:
The oil industry has three levels: upstream, midstream, and downstream which encompass the main segments in the supply chain. The upstream level includes the exploration, drilling, and production of crude oil and the midstream level includes the transportation and trading of crude oil to refineries. The downstream level refers to the refining of crude oil into finished product, the storage of crude oil, and the distribution and marketing of crude oil to wholesalers and retailers.

http://www.quarnelbriefs.example/images/value_chain.gif
http://www.tarvoskilearn.example/modules/m008/imgs/fig_001.jpg
Here is another that is more for reference:

http://www.hollin.example/web/soc142/team9/GVC_clip_image002.jpg

https://www.zembrafind.example/search?q=oil+value+chain&hl=en&tbo=u&prmd=imvns&tbm=isch&source=univ&sa=X&ei=I1hsUOuEC-SK2wXry4DAAg&ved=0CDMQsAQ&biw=1680&bih=925

```html
<!DOCTYPE html>
<html lang="en">
<head>
<meta charset="utf-8">
<title>Oil Supply Chain</title>
<link rel="stylesheet" href="https://fonts.googleapis.com/css2?family=Signika:wght@700&display=swap">
<style>
  :root {
    --bar: #000000;
    --title: #ffffff;
    --ink: #0d0d0d;
    --sky-top: #6fb6dd;
    --sky-mid: #cfe7f3;
    --sky-low: #f2f7f8;
    --hill: #8c9a86;
    --frame: #ffffff;
  }
  html, body {
    margin: 0;
    padding: 0;
    overflow: hidden;
    background: #ffffff;
  }
  .banner {
    position: relative;
    width: 1200px;
    height: 500px;
    overflow: hidden;
    font-family: "Signika", "Trebuchet MS", sans-serif;
    font-weight: 700;
    color: var(--ink);
    background: linear-gradient(180deg, var(--sky-top) 0%, var(--sky-mid) 35%, var(--sky-low) 62%, var(--hill) 100%);
    box-shadow: inset 0 0 0 2px #000;
  }
  .backdrop {
    position: absolute;
    left: 0; top: 0; width: 100%; height: 100%;
  }
  .title-bar {
    position: absolute;
    left: 0; top: 0;
    width: 100%; height: 63px;
    background: var(--bar);
    display: flex;
    align-items: center;
    justify-content: center;
  }
  .title-bar h1 {
    margin: 0;
    color: var(--title);
    font-size: 50px;
    letter-spacing: 1px;
    line-height: 1;
  }
  .stage-heading {
    position: absolute;
    top: 76px;
    margin: 0;
    font-size: 43px;
    line-height: 1;
    transform: translateX(-50%);
    white-space: nowrap;
  }
  .stage-caption {
    position: absolute;
    top: 385px;
    margin: 0;
    font-size: 37px;
    line-height: 52px;
    text-align: center;
    transform: translateX(-50%);
    white-space: nowrap;
  }
  .photo {
    position: absolute;
    border: 3px solid var(--frame);
    box-sizing: border-box;
  }
  .photo--upstream {
    left: 37px; top: 140px; width: 302px; height: 230px;
    background: linear-gradient(180deg, #d7dde3 0%, #c4ccd2 45%, #5f8a3c 60%, #4f7a31 100%);
  }
  .photo--midstream {
    left: 427px; top: 140px; width: 320px; height: 230px;
    background: linear-gradient(180deg, #c9a9a4 0%, #a9a5b6 40%, #4d5e78 70%, #1d2a3a 100%);
  }
  .photo--downstream {
    left: 822px; top: 187px; width: 343px; height: 138px;
    background: linear-gradient(180deg, #dfe6ea 0%, #b9c4c8 45%, #8e9a88 65%, #6f7470 100%);
  }
  .arrows {
    position: absolute;
    left: 0; top: 0;
    pointer-events: none;
  }
</style>
</head>
<body>
  <div class="banner">
    <div class="backdrop" role="img" aria-label="Pale sky above a hazy green mountain ridge"></div>

    <header class="title-bar"><h1>OIL SUPPLY CHAIN</h1></header>

    <h2 class="stage-heading" style="left:187px">UPSTREAM</h2>
    <h2 class="stage-heading" style="left:597px">MIDSTREAM</h2>
    <h2 class="stage-heading" style="left:995px">DOWNSTREAM</h2>

    <div class="photo photo--upstream" role="img" aria-label="Oil derrick on a grassy field under an overcast sky"></div>
    <div class="photo photo--midstream" role="img" aria-label="Refinery towers silhouetted against a dusky sky"></div>
    <div class="photo photo--downstream" role="img" aria-label="Roadside fuel station with pumps under a canopy"></div>

    <svg class="arrows" width="1200" height="500" viewBox="0 0 1200 500" aria-hidden="true">
      <defs>
        <marker id="arrow-head" viewBox="0 0 10 10" refX="3" refY="5" markerWidth="3.2" markerHeight="3.2" orient="auto">
          <path d="M0,0 L10,5 L0,10 Z" fill="#000"/>
        </marker>
      </defs>
      <path d="M285,185 Q390,105 462,200" fill="none" stroke="#000" stroke-width="15" stroke-linecap="round" marker-end="url(#arrow-head)"/>
      <path d="M705,332 Q860,430 972,318" fill="none" stroke="#000" stroke-width="15" stroke-linecap="round" marker-end="url(#arrow-head)"/>
    </svg>

    <p class="stage-caption" style="left:187px">Exploration &amp;<br>Production</p>
    <p class="stage-caption" style="left:587px">Transportation &amp;<br>Refining / Processing</p>
    <p class="stage-caption" style="left:995px">Distribution &amp;<br>Retail Sale</p>
  </div>
</body>
</html>
```